Surgery Office Letterhead Design

I'm seeking new letterhead that will comprise all of our office locations and logo and other applicable information, per the following:

Office Locations:

Bluewater Institute for Oral & Facial Surgery at Harlow Springs
347 Amberly Lane
Harlow Springs, Texas 75058
Phone 817.392.4806
Fax 817.392.7734

Bluewater Institute for Oral & Facial Surgery at Millbrook
588 Quarry Hollow Parkway
Millbrook, Texas 75428
Phone 254.763.2248
Fax 254.763.2251

Bluewater Institute for Oral & Facial Surgery at Cedar Ridge
715 West 9th Street
Cedar Ridge, Texas 75537
Phone 254.481.6072
Fax 254.481.6079

Other Info to include:

www.bluewatermaxillo.example
hello@bluewatermaxillo.example

Industry/Entity Type

Medical

Font styles to use
Serif
Sans Serif

Requirements
Must have
• See Project Description

```html
<!DOCTYPE html>
<html lang="en">
<head>
<meta charset="utf-8">
<title>Bluewater Institute Letterhead</title>
<link href="https://fonts.googleapis.com/css2?family=Cinzel:wght@500&family=Open+Sans:wght@400;700&display=swap" rel="stylesheet">
<style>
  :root {
    --backdrop: #e8e8ea;
    --paper: #ffffff;
    --brand-blue: #5f7399;
    --brand-blue-light: #a9b4c8;
    --ink-dark: #2c3140;
    --on-blue: #ffffff;
  }
  * { margin: 0; padding: 0; box-sizing: border-box; }
  html, body { width: 1200px; height: 795px; overflow: hidden; }
  body { background: var(--backdrop); font-family: "Open Sans", sans-serif; }
  .letterhead {
    position: absolute; left: 320px; top: 35px;
    width: 560px; height: 725px;
    background: var(--paper);
    box-shadow: 0 4px 18px rgba(0,0,0,0.12);
    overflow: hidden;
  }
  .corner-square {
    position: absolute; left: 0; top: 74px;
    width: 30px; height: 32px;
    background: var(--brand-blue-light);
  }
  .brand {
    position: absolute; left: 42px; top: 70px;
    font-family: "Cinzel", serif; font-weight: 500;
    color: var(--ink-dark); line-height: 1;
  }
  .brand-name { font-size: 15px; letter-spacing: 0.5px; }
  .brand-tagline { font-size: 7px; letter-spacing: 0.6px; margin-top: 3px; }
  .header-band {
    position: absolute; left: 225px; top: 18px;
    width: 335px; height: 58px;
    background: var(--brand-blue);
  }
  .header-contact {
    position: absolute; right: 18px; top: 10px;
    color: var(--on-blue); font-size: 7.5px; line-height: 12px;
  }
  .header-contact li { list-style: none; display: flex; align-items: center; gap: 5px; }
  .header-contact svg { width: 7px; height: 7px; }
  .footer-wave { position: absolute; left: 0; top: 0; width: 560px; height: 725px; }
  .office {
    position: absolute; width: 170px;
    color: var(--on-blue); text-align: center;
    font-size: 7.5px; line-height: 10.5px;
  }
  .office-name { font-weight: 700; font-size: 7px; line-height: 9.5px; margin-bottom: 2px; }
  .office--cedar-ridge { left: 18px; top: 630px; }
  .office--harlow-springs { left: 198px; top: 612px; }
  .office--millbrook { left: 378px; top: 580px; }
  .office-divider {
    position: absolute; width: 1px; height: 62px;
    background: rgba(255,255,255,0.55);
  }
  .office-divider--one { left: 192px; top: 628px; }
  .office-divider--two { left: 372px; top: 604px; }
</style>
</head>
<body>
  <main class="letterhead">
    <div class="header-band">
      <ul class="header-contact">
        <li>
          <svg viewBox="0 0 10 10"><circle cx="5" cy="5" r="4" fill="none" stroke="#fff" stroke-width="1.2"/><line x1="1" y1="5" x2="9" y2="5" stroke="#fff" stroke-width="1"/></svg>
          www.bluewatermaxillo.example
        </li>
        <li>
          <svg viewBox="0 0 10 10"><rect x="0.5" y="2" width="9" height="6" fill="none" stroke="#fff" stroke-width="1.1"/><polyline points="0.5,2 5,5.5 9.5,2" fill="none" stroke="#fff" stroke-width="1"/></svg>
          hello@bluewatermaxillo.example
        </li>
      </ul>
    </div>

    <div class="corner-square"></div>
    <div class="brand">
      <div class="brand-name">BLUEWATER INSTITUTE</div>
      <div class="brand-tagline">FOR ORAL &amp; FACIAL SURGERY</div>
    </div>

    <svg class="footer-wave" viewBox="0 0 560 725" aria-hidden="true">
      <path d="M0,592 Q230,660 560,498 L560,725 L0,725 Z" fill="var(--brand-blue)"/>
      <path d="M0,586 Q230,654 560,492" fill="none" stroke="var(--brand-blue)" stroke-width="1"/>
      <path d="M0,596 Q230,664 560,502" fill="none" stroke="#ffffff" stroke-width="1"/>
    </svg>

    <section class="office office--cedar-ridge">
      <p class="office-name">Bluewater Institute for<br>Oral &amp; Facial Surgery at Cedar Ridge</p>
      <p>715 West 9th Street</p>
      <p>Cedar Ridge, Texas 75537</p>
      <p>Phone : 254.481.6072</p>
      <p>Fax : 254.481.6079</p>
    </section>
    <div class="office-divider office-divider--one"></div>
    <section class="office office--harlow-springs">
      <p class="office-name">Bluewater Institute for<br>Oral &amp; Facial Surgery at Harlow Springs</p>
      <p>347 Amberly Lane</p>
      <p>Harlow Springs, Texas 75058</p>
      <p>Phone : 817.392.4806</p>
      <p>Fax : 817.392.7734</p>
    </section>
    <div class="office-divider office-divider--two"></div>
    <section class="office office--millbrook">
      <p class="office-name">Bluewater Institute for<br>Oral &amp; Facial Surgery at Millbrook</p>
      <p>588 Quarry Hollow Parkway</p>
      <p>Millbrook, Texas 75428</p>
      <p>Phone : 254.763.2248</p>
      <p>Fax : 254.763.2251</p>
    </section>
  </main>
</body>
</html>
```